Business cards, letter head, stationery
trial lawyer
Bright & Fun-filled
Teodoro Villaseca
Trial Lawyer
2716 kelverham, suite 300
Bellaire Texas 77538
Tevmilux@quarnela.com
Need to include:
Offices in Houston , San Antonio, and eagle pass Texas
Use winning logo

```html
<!DOCTYPE html>
<html lang="en">
<head>
<meta charset="utf-8">
<title>Teodoro Villaseca — Stationery</title>
<link href="https://fonts.googleapis.com/css2?family=Cinzel:wght@600;700&family=Open+Sans:wght@400;600&display=swap" rel="stylesheet">
<style>
  :root{
    --navy:#1d3f86;
    --blue:#2a5fb0;
    --orange:#f07a1a;
    --orange-light:#f7a045;
    --paper:#ffffff;
    --grey:#c9ccd2;
    --ink:#4a4f58;
    --stage:#e4e5e8;
  }
  *{box-sizing:border-box;margin:0;padding:0}
  html,body{width:1200px;height:842px;overflow:hidden;background:var(--stage)}
  body{position:relative;font-family:"Open Sans",Arial,sans-serif;color:var(--ink)}
  .piece{position:absolute;background:var(--paper);box-shadow:0 2px 8px rgba(0,0,0,.18);overflow:hidden}
  .piece svg.swoosh{position:absolute;left:0;width:100%;z-index:0}
  .mark{display:inline-block;background:var(--navy);flex:none}
  .brand{display:flex;align-items:center;gap:8px;position:relative;z-index:2}
  .brand-name{font-family:"Cinzel",Georgia,serif;font-weight:700;color:var(--navy);line-height:1.05;letter-spacing:.5px;white-space:nowrap}
  .brand-sub{font-family:"Cinzel",Georgia,serif;font-weight:700;color:var(--navy);letter-spacing:2px;white-space:nowrap}

  /* envelope backs */
  .env-back{left:60px;width:240px;height:95px}
  .env-back .mark{position:absolute;left:105px;top:20px;width:30px;height:30px;background:#fff;border:3px solid rgba(255,255,255,.6)}
  .env-back.white .mark{background:var(--navy)}

  /* letterhead */
  .letterhead{left:290px;top:70px;width:435px;height:740px;padding:34px 40px}
  .letterhead .brand{margin-left:8px}
  .letterhead .mark{width:24px;height:24px}
  .letterhead .brand-name{font-size:15px}
  .letterhead .brand-sub{font-size:8px}
  .tagline{font-size:5px;color:var(--navy);letter-spacing:1px}
  .recipient{margin-top:30px;font-size:9.5px;line-height:1.35}
  .salutation{margin-top:12px;font-size:9.5px}
  .letter-body p{margin-top:9px;font-size:8px;line-height:1.45;color:#6a6e76}
  .signoff{margin-top:14px;font-size:8px;color:#6a6e76}
  .signature{margin-top:6px;width:60px;height:16px;background:linear-gradient(90deg,#d7d9de,#eceef1)}
  .watermark{position:absolute;right:45px;top:390px;width:110px;height:110px;border:2px solid #eef0f3;background:#f7f8fa;z-index:0}
  .letter-footer{position:absolute;left:160px;bottom:80px;font-size:6px;color:var(--navy);line-height:1.4;z-index:2}

  /* envelope front */
  .env-front{left:40px;top:470px;width:480px;height:230px;padding:40px 30px}
  .env-front .mark{width:28px;height:28px}
  .env-front .brand-name{font-size:16px}
  .env-front .brand-sub{font-size:8px}
  .env-front .addr{position:relative;z-index:2;margin-top:8px;font-size:5.5px;color:var(--navy)}
  .env-front .ghost{position:absolute;left:340px;top:25px;width:80px;height:80px;border:2px solid #f0f1f4;background:#f8f9fb;z-index:0}

  /* cards */
  .card{left:785px;width:225px;height:125px}
  .card .lines{position:absolute;left:120px;top:42px;font-size:5.5px;line-height:1.5;z-index:2}
  .card.white .lines{color:var(--navy)}
  .card.orange{background:var(--orange)}
  .card.orange .lines,.card.blue .lines{color:#fff}
  .card.blue{background:var(--navy)}
  .card .mark{position:absolute;left:120px;top:18px;width:16px;height:16px}
  .card.orange .mark,.card.blue .mark{background:#fff}
  .card.front .brand{position:absolute;left:14px;top:16px;gap:6px}
  .card.front .mark{position:static;width:18px;height:18px}
  .card.front .brand-name{font-size:9px}
  .card.front .brand-sub{font-size:5px}
  .card.front .contact{position:absolute;left:14px;top:56px;font-size:5.5px;color:var(--navy);line-height:1.5;z-index:2}
  .card.front .holder{position:absolute;right:14px;top:70px;font-size:8px;font-weight:600;color:var(--orange);z-index:2}
</style>
</head>
<body>

<!-- envelope back flaps -->
<div class="piece env-back white" style="top:55px">
  <svg class="swoosh" style="top:0;height:95px" viewBox="0 0 240 95" preserveAspectRatio="none">
    <path d="M0 0 L120 60 L240 0" fill="none" stroke="var(--grey)" stroke-width="2"/>
  </svg>
  <span class="mark"></span>
</div>
<div class="piece env-back" style="top:140px;background:var(--orange)">
  <svg class="swoosh" style="top:0;height:95px" viewBox="0 0 240 95" preserveAspectRatio="none">
    <path d="M0 0 L120 70 L240 0 Z" fill="var(--orange-light)"/>
  </svg>
  <span class="mark"></span>
</div>
<div class="piece env-back" style="top:225px;background:var(--navy)">
  <svg class="swoosh" style="top:0;height:95px" viewBox="0 0 240 95" preserveAspectRatio="none">
    <path d="M0 0 L120 70 L240 0 Z" fill="var(--blue)"/>
  </svg>
  <span class="mark"></span>
</div>

<!-- letterhead -->
<section class="piece letterhead">
  <div class="brand">
    <span class="mark"></span>
    <div>
      <div class="brand-name">TEODORO VILLASECA</div>
      <div class="brand-sub">ATTORNEY AT LAW</div>
      <div class="tagline">A TRIAL LAW PRACTICE</div>
    </div>
  </div>
  <div class="recipient">Someone Some body,<br>100 Long St<br>Brisbane, Australia</div>
  <div class="salutation">Dear Someone Somebody,</div>
  <div class="letter-body">
    <p>Lorem ipsum dolor sit amet, consectetuer adipiscing elit, sed diam nonummy nibh euismod tincidunt ut laoreet dolore magna aliquam erat volutpat. Ut wisi enim ad minim veniam, quis nostrud exerci tation ullamcorper suscipit lobortis nisl ut aliquip ex ea commodo consequat. Duis autem vel eum iriure dolor in hendrerit in vulputate velit esse molestie consequat, vel illum dolore eu feugiat nulla facilisis at vero eros et accumsan et iusto odio dignissim qui blandit praesent luptatum zzril delenit augue duis dolore te feugait nulla facilisi.</p>
    <p>Lorem ipsum dolor sit amet, consectetuer adipiscing elit, sed diam nonummy nibh euismod tincidunt ut laoreet dolore magna aliquam erat volutpat. Ut wisi enim ad minim veniam, quis nostrud exerci tation ullamcorper suscipit lobortis nisl ut aliquip ex ea commodo consequat. Duis autem vel eum iriure dolor in hendrerit in vulputate velit esse molestie consequat, vel illum dolore eu feugiat nulla facilisis at vero eros et accumsan et iusto odio dignissim qui blandit praesent.</p>
    <p>Lorem ipsum dolor sit amet, consectetuer adipiscing elit, sed diam nonummy nibh euismod tincidunt ut laoreet dolore magna aliquam erat volutpat. Ut wisi enim ad minim veniam, quis nostrud exerci tation ullamcorper suscipit lobortis nisl ut aliquip ex ea commodo consequat. Duis autem vel eum iriure dolor in hendrerit in vulputate velit esse molestie consequat.</p>
  </div>
  <div class="signoff">Yours Sincerely,<br>Teodoro Villaseca</div>
  <div class="signature" role="img" aria-label="Handwritten signature"></div>
  <div class="watermark"></div>
  <svg class="swoosh" style="bottom:0;height:80px" viewBox="0 0 435 80" preserveAspectRatio="none">
    <path d="M0 10 Q200 80 435 20 L435 80 L0 80 Z" fill="var(--orange)"/>
    <path d="M0 28 Q200 92 435 40 L435 80 L0 80 Z" fill="var(--navy)"/>
    <path d="M0 38 Q200 100 435 52 L435 80 L0 80 Z" fill="#fff"/>
  </svg>
  <div class="letter-footer">2716 kelverham, suite 300 Bellaire Texas 77538<br>T: 713-555-0142 &nbsp;|&nbsp; www.villasecatriallaw.com</div>
</section>

<!-- envelope front -->
<section class="piece env-front">
  <div class="ghost"></div>
  <div class="brand">
    <span class="mark"></span>
    <div>
      <div class="brand-name">TEODORO VILLASECA</div>
      <div class="brand-sub">ATTORNEY AT LAW</div>
    </div>
  </div>
  <div class="addr">2716 kelverham, suite 300 Bellaire Texas 77538</div>
  <svg class="swoosh" style="bottom:0;height:120px" viewBox="0 0 480 120" preserveAspectRatio="none">
    <path d="M180 120 Q360 90 480 0 L480 120 Z" fill="var(--orange)"/>
    <path d="M220 120 Q390 100 480 20 L480 120 Z" fill="var(--navy)"/>
  </svg>
</section>

<!-- business cards -->
<div class="piece card white" style="top:200px">
  <span class="mark"></span>
  <div class="lines">Houston office in Bellaire<br>2716 kelverham, suite 300<br>Bellaire Texas 77538</div>
  <svg class="swoosh" style="bottom:0;height:30px" viewBox="0 0 225 30" preserveAspectRatio="none">
    <path d="M0 30 Q110 0 225 18 L225 30 Z" fill="var(--navy)"/>
  </svg>
</div>
<div class="piece card orange" style="top:355px">
  <span class="mark"></span>
  <div class="lines">San Antonio office<br>2716 kelverham, suite 300<br>San Antonio Texas</div>
</div>
<div class="piece card blue" style="top:510px">
  <span class="mark"></span>
  <div class="lines">Eagle Pass office<br>2716 kelverham, suite 300<br>Eagle Pass Texas</div>
</div>
<div class="piece card white front" style="top:665px">
  <div class="brand">
    <span class="mark"></span>
    <div>
      <div class="brand-name">TEODORO VILLASECA</div>
      <div class="brand-sub">ATTORNEY AT LAW</div>
    </div>
  </div>
  <div class="contact">T: 713-555-0142<br>Tevmilux@quarnela.com<br>www.villasecatriallaw.com</div>
  <div class="holder">Teodoro Villaseca</div>
  <svg class="swoosh" style="bottom:0;height:30px" viewBox="0 0 225 30" preserveAspectRatio="none">
    <path d="M0 10 Q110 34 225 8 L225 30 L0 30 Z" fill="var(--orange)"/>
    <path d="M0 18 Q110 40 225 16 L225 30 L0 30 Z" fill="var(--navy)"/>
  </svg>
</div>

</body>
</html>
```